TRI Fold FLYER DESIGN

We would like a Tri Fold Flyer that represents our unique business. Needs to flow. By this I mean the way the flyer folds out the messages need to flow correctly into the next page, be well balanced. bright and colourful and be very effective at getting our USP across.
I have tried Q lane before and was not happy with the outcome hence again sceptical about going down this similar path.
I have attached some of the content in the two screen shots.
Also check out the website to get a further understanding of our unique model/ concept and appearance/ theme.

With a combined 30+ years of experience in their professional back grounds Morris and Dylan have extracted the best practices and methodology and have developed a revolutionary training system that is designed to deliver maximum results in minimum time.

```html
<!DOCTYPE html>
<html lang="en">
<head>
<meta charset="utf-8">
<title>Summit Pulse Fitness – Tri-fold Flyer</title>
<link rel="stylesheet" href="https://fonts.googleapis.com/css2?family=Open+Sans:wght@400;600;700;800&family=Passion+One:wght@400;700&display=swap">
<style>
  :root{
    --blue-deep:#0b3d91;
    --blue:#1565c0;
    --blue-mid:#1e88e5;
    --sky-top:#bfe3f8;
    --sky-low:#eaf6fd;
    --orange:#f7941d;
    --yellow:#ffd200;
    --ink:#333c48;
    --white:#ffffff;
    --stage:#8a8d91;
    --red:#e53935;
    --green:#43a047;
    --teal:#1e9bd7;
  }
  *{box-sizing:border-box;margin:0;padding:0}
  html,body{width:1200px;height:1000px;overflow:hidden}
  body{background:var(--stage);font-family:"Open Sans",sans-serif;color:var(--ink);position:relative}
  .spread{position:absolute;left:30px;top:118px;width:1140px;height:764px;display:flex;box-shadow:0 10px 30px rgba(0,0,0,.35)}
  .panel{position:relative;width:380px;height:764px;overflow:hidden}
  .panel-bg{position:absolute;inset:0;width:100%;height:100%}
  .abs{position:absolute}
  .photo{position:absolute;background:linear-gradient(160deg,#d9c2a8,#9fb7c9)}
  .photo.round{border-radius:50%;border:3px solid var(--white)}

  /* team panel */
  .team-title{left:0;top:26px;width:100%;text-align:center;color:var(--white);font-size:20px;font-weight:600}
  .team-title span{color:var(--yellow)}
  .trainers{left:40px;top:80px;width:300px;display:flex;justify-content:space-between}
  .trainer{width:80px;text-align:center;font-size:8px;font-weight:700;color:var(--blue-deep)}
  .trainer .photo{position:relative;width:60px;height:60px;margin:0 auto 4px}
  .team-copy{left:22px;top:170px;width:336px;font-size:10.5px;line-height:1.55}
  .programs-title{left:0;top:350px;width:100%;text-align:center;color:var(--orange);font-size:11px;font-weight:700}
  .prices{left:22px;top:372px;width:336px;display:flex;gap:6px}
  .price{flex:1;border:1px solid #ddd;background:#fafafa;text-align:center;font-size:7.5px}
  .price .head{color:var(--white);font-weight:700;padding:3px 0}
  .price .amt{font-size:16px;font-weight:800;padding:5px 0 2px}
  .price .note{padding:2px 4px 6px;line-height:1.3}
  .call-badge{left:80px;top:640px;width:220px;height:86px;background:var(--yellow);border-radius:14px;border:3px solid var(--white);text-align:center;padding-top:8px}
  .call-badge .big{font-family:"Passion One",sans-serif;font-size:38px;color:var(--blue-deep);line-height:1}
  .call-badge .num{font-size:15px;font-weight:800;color:var(--blue-deep);margin-top:4px}

  /* middle panel */
  .mid-title{left:22px;top:22px;width:340px;color:var(--blue);font-size:15px;font-weight:600}
  .mid-copy{left:22px;top:52px;width:336px;font-size:10.5px;line-height:1.55}
  .h-orange{color:var(--orange);font-weight:700;font-size:11px}
  .block{left:22px;width:336px;font-size:10.5px;line-height:1.7}
  .dot-list{list-style:none}
  .dot-list li{position:relative;padding-left:14px}
  .dot-list li::before{content:"";position:absolute;left:0;top:6px;width:7px;height:7px;border-radius:50%;background:var(--orange)}
  .formula-icons{left:40px;top:468px;width:300px;height:28px;background:linear-gradient(90deg,#cfe3f6,#e6f1fb);border-radius:4px}
  .formula{left:22px;top:502px;width:336px;display:flex;align-items:center;justify-content:center;gap:8px;font-weight:800;color:var(--blue);font-size:13px;text-align:center;line-height:1.05}
  .formula small{display:block;font-size:8px;font-weight:700}
  .formula .op{font-size:18px;color:var(--blue-deep)}
  .formula .total{color:var(--red)}
  .contact{left:40px;top:708px;width:320px;color:var(--white);font-size:8.5px;line-height:1.5}
  .contact b{color:var(--yellow);font-weight:600}

  /* cover panel */
  .brand{left:0;top:36px;width:100%;display:flex;justify-content:center;align-items:center;gap:10px}
  .brand-mark{width:34px;height:34px;background:var(--yellow);border-radius:4px}
  .brand-name{color:var(--yellow);font-weight:800;font-size:19px;line-height:1.05;letter-spacing:.5px}
  .welcome{left:0;top:138px;width:100%;text-align:center;font-family:"Passion One",sans-serif}
  .welcome .w1{font-size:36px;color:var(--white);-webkit-text-stroke:1.5px var(--blue-deep);line-height:1}
  .welcome .row{display:flex;justify-content:center;align-items:center;gap:4px}
  .welcome .the{writing-mode:vertical-rl;transform:rotate(180deg);font-size:15px;color:var(--orange);line-height:1}
  .welcome .rev{font-size:46px;color:var(--blue);line-height:.95}
  .welcome .wo{font-size:44px;color:var(--orange);line-height:.95}
  .welcome .of{writing-mode:vertical-rl;transform:rotate(180deg);font-size:15px;color:var(--blue);line-height:1}
  .cover-list{left:22px;top:398px;width:200px;font-size:11px;line-height:1.9;color:var(--blue-deep);font-weight:600}
</style>
</head>
<body>
<main class="spread">

  <!-- Inside left: team -->
  <section class="panel team">
    <svg class="panel-bg" viewBox="0 0 380 764" preserveAspectRatio="none" aria-hidden="true">
      <rect width="380" height="764" fill="#1565c0"/>
      <path d="M0 70 Q190 55 380 70 L380 640 Q190 600 0 660 Z" fill="#ffffff"/>
      <path d="M0 660 Q190 600 380 640 L380 652 Q190 612 0 672 Z" fill="#f7941d"/>
    </svg>
    <h2 class="abs team-title">Dedicated <span>training</span> team</h2>
    <div class="abs trainers">
      <div class="trainer"><div class="photo round" role="img" aria-label="Portrait photo of trainer Dylan"></div>Dylan Head Trainer</div>
      <div class="trainer"><div class="photo round" role="img" aria-label="Portrait photo of trainer Morris"></div>Morris Head Trainer</div>
      <div class="trainer"><div class="photo round" role="img" aria-label="Portrait photo of a team trainer"></div>Team Trainer</div>
    </div>
    <p class="abs team-copy">The team at Summit Pulse Fitness have put over 30 years of combined experience in fitness and training into this revolutionary new training system that is helping residence on the Northern Beaches to look and feel a Summit Pulse in just half the time. Adding to this, every one of your workouts has a qualified personal trainer to help guide you, correct your technique and progress or regress your program to suit your individual level of skill and ability. Most importantly we keep it fun all whilst keeping you motivated and accountable to maximise your results. The program changes daily so you never do the same work out twice.</p>
    <h3 class="abs programs-title">Summit Pulse Fitness Programs</h3>
    <div class="abs prices">
      <div class="price"><div class="head" style="background:var(--red)">STARTER</div><div class="amt" style="color:var(--red)">$59 p/w</div><div class="note">Unlimited Sessions Weekly</div></div>
      <div class="price"><div class="head" style="background:var(--orange)">REGULAR</div><div class="amt" style="color:var(--orange)">$58 p/w</div><div class="note">Unlimited Sessions 3 Months</div></div>
      <div class="price"><div class="head" style="background:var(--green)">COMMIT</div><div class="amt" style="color:var(--green)">$49 p/w</div><div class="note">Unlimited Sessions 6 Months</div></div>
      <div class="price"><div class="head" style="background:var(--teal)">YEARLY</div><div class="amt" style="color:var(--teal)">$45 p/w</div><div class="note">Unlimited Sessions 12 Months</div></div>
    </div>
    <div class="photo" role="img" aria-label="Photo of a woman doing a push-up" style="left:60px;top:470px;width:260px;height:150px;background:linear-gradient(180deg,#ffffff,#e9eef3 60%,#cdd8e2);border:none"></div>
    <div class="abs call-badge">
      <div class="big">CALL NOW!</div>
      <div class="num">Call: (02) 9000 1234</div>
    </div>
  </section>

  <!-- Inside middle: method -->
  <section class="panel method">
    <svg class="panel-bg" viewBox="0 0 380 764" preserveAspectRatio="none" aria-hidden="true">
      <rect width="380" height="764" fill="#ffffff"/>
      <path d="M0 680 Q190 640 380 660 L380 764 L0 764 Z" fill="#1565c0"/>
      <path d="M0 672 Q190 632 380 652 L380 662 Q190 642 0 682 Z" fill="#f7941d"/>
    </svg>
    <h2 class="abs mid-title">Never train without a personal trainer again.</h2>
    <p class="abs mid-copy">Our Personal Trainers are there to guide you, correct your technique and most importantly we keep you motivated and accountable to maximise your results! Your program changes daily. Our experienced trainers can modify the program to suit you individual needs.</p>
    <div class="abs block" style="top:140px">
      <p class="h-orange">What do we do?</p>
      <p>High tempo, task oriented training.</p>
      <p>Get you in and out the door in 31 Minutes.</p>
      <p class="h-orange">Why are we Different?</p>
      <p>No bookings required, workouts start every 3 ½ Minutes</p>
      <p>Trainer with you all the way every day!</p>
      <ul class="dot-list">
        <li>No Mirrors</li>
        <li>No Machines</li>
        <li>No Ego's</li>
        <li>No BS – Just results!</li>
      </ul>
    </div>
    <div class="photo round" role="img" aria-label="Photo of the two trainers" style="left:250px;top:258px;width:76px;height:76px"></div>
    <p class="abs block" style="top:388px;line-height:1.55">With a combined 30+ years of experience in their professional back grounds Morris and Dylan have extracted the best practices and methodology and have developed a revolutionary training system that is designed to deliver maximum results in minimum time.</p>
    <div class="abs formula-icons" role="img" aria-label="Row of small exercise figure icons"></div>
    <div class="abs formula">
      <span>3 minutes<small>EACH</small></span><span class="op">+</span>
      <span>30 seconds<small>REST</small></span><span class="op">×</span>
      <span>9 training<small>STATIONS</small></span><span class="op">=</span>
      <span class="total">31 minutes<small>TOTAL</small></span>
    </div>
    <div class="photo" role="img" aria-label="Photo of two trainers stretching on a yellow circle" style="left:110px;top:560px;width:160px;height:130px;border-radius:80px 80px 0 0;background:radial-gradient(circle at 50% 80%,#ffd200,#f7941d)"></div>
    <div class="abs contact">
      <b>How to contact us</b><br>
      Shop 4, 120 Harbour Road - Seaview, NSW, 2000<br>
      Call: (02) 9000 1234 · hello@summitpulsefitness.example
    </div>
  </section>

  <!-- Front cover -->
  <section class="panel cover">
    <svg class="panel-bg" viewBox="0 0 380 764" preserveAspectRatio="none" aria-hidden="true">
      <defs>
        <linearGradient id="sky" x1="0" y1="0" x2="0" y2="1">
          <stop offset="0" stop-color="#bfe3f8"/><stop offset="1" stop-color="#eaf6fd"/>
        </linearGradient>
      </defs>
      <rect width="380" height="764" fill="#1565c0"/>
      <path d="M0 130 Q190 90 380 110 L380 690 Q190 640 0 700 Z" fill="url(#sky)"/>
      <path d="M0 118 Q190 78 380 98 L380 110 Q190 90 0 130 Z" fill="#f7941d"/>
      <path d="M0 700 Q190 640 380 690 L380 700 Q190 652 0 712 Z" fill="#f7941d"/>
      <path d="M30 260 A170 170 0 0 1 360 200" fill="none" stroke="#ffffff" stroke-opacity=".6" stroke-width="6"/>
    </svg>
    <div class="abs brand">
      <div class="brand-mark"></div>
      <div class="brand-name">SUMMIT PULSE<br>FITNESS</div>
    </div>
    <div class="photo" role="img" aria-label="Photo of a woman in a white tank top lifting a kettlebell" style="left:220px;top:330px;width:150px;height:350px;border-radius:60px 60px 10px 10px;background:linear-gradient(180deg,#e9d4c2,#f4f1ec 45%,#6fc3e8)"></div>
    <div class="abs welcome">
      <div class="w1">Welcome to</div>
      <div class="row"><span class="the">THE</span><span class="rev">REVOLUTION</span></div>
      <div class="row"><span class="of">OF</span><span class="wo">WORKING OUT</span></div>
    </div>
    <ul class="abs cover-list dot-list">
      <li>Unlimited 31 Minute Workouts.</li>
      <li>Elite level Trainers.</li>
      <li>Workouts start every 3½ Minutes.</li>
      <li>Programs for everyone.</li>
      <li>No Bookings required.</li>
    </ul>
  </section>

</main>
</body>
</html>
```